Heavy Equipment Service Technician

K&T Equipment Corp. is a family owned industry leader that’s been supplying construction equipment, tractors and landscaping gear to Southern Connecticut for the past 81 years. Located on Route 48 in Orange, we help home builders, site excavators, road builders, municipalities, landscapers, home owners and many more. We believe we can make work fun and easy by supplying new and used equipment, equipment rentals, service, parts and advice. Our fast paced service department is ready to expand! We are looking for a Heavy Equipment Service Technician, Experience Required.

QUALIFICATIONS AND SKILL:

· Must have a valid driver’s license.

· Must be reliable, hard working and have a professional work ethic.

· Must own tools and have the ability to work independently.

· Must have the ability to lift, push, pull 70+ pounds, climb heavy. equipment safely, bend and kneel.

· Must be able to perform basic equipment service: ie: filters, oils, inspections.

· Must possess a willingness to learn and grow.

· Must provide own tools.

RESPONSIBILITIES AND DUTIES:

· Perform scheduled services on heavy equipment and tractors.

· Perform final assembly of tractors.

· Perform body work on equipment.

· Perform minor welding on equipment and tractors.

· Keep work space clean of all debris.

Hi, This, is my first time using Pixel Guild! I am looking to design a new web page on our website that I can direct prospective employees. This webpage I want to look very professional to attract new employees. I am hoping to show off the wonderful benefits we offer, the fun work place and a great place to grow.

```html
<!DOCTYPE html>
<html lang="en">
<head>
<meta charset="utf-8">
<title>Heavy Equipment Service Technician | Harrow Machinery</title>
<link href="https://fonts.googleapis.com/css2?family=Outfit:wght@300;400;500;600;700;800&display=swap" rel="stylesheet">
<style>
:root{
  --yellow:#FFD400;
  --ink:#111a26;
  --navy:#0f1f35;
  --text:#2b3340;
  --muted:#5b6370;
  --bg-soft:#f5f6f8;
  --field:#eeeeef;
  --white:#ffffff;
}
*{box-sizing:border-box;margin:0;padding:0}
html,body{width:1200px;height:3399px;overflow:hidden}
body{font-family:'Outfit',sans-serif;color:var(--text);background:var(--white);position:relative}

/* hero */
.hero-photo{position:absolute;left:0;top:0;width:1200px;height:770px;
  clip-path:polygon(0 0,1200px 0,1200px 330px,436px 770px,0 519px);
  background:linear-gradient(120deg,#3a3016 0%,#6b5414 35%,#a8840f 55%,#3e3a33 75%,#1f2026 100%)}
.brand{position:absolute;left:125px;top:0;width:82px;height:106px;background:var(--white);
  display:flex;flex-direction:column;align-items:center;justify-content:center;gap:6px}
.brand-mark{width:26px;height:26px;background:var(--yellow)}
.brand-name{font-size:11px;font-weight:700;color:var(--ink);text-align:center;line-height:1.15}
.nav{position:absolute;top:25px;display:flex;gap:45px;left:664px}
.nav a{color:var(--white);text-decoration:none;font-size:18px}
.phone-btn{position:absolute;left:927px;top:18px;width:142px;height:35px;border-radius:18px;background:var(--yellow);
  color:var(--white);font-size:11px;font-weight:600;display:flex;align-items:center;justify-content:center;gap:5px}
.hero-title{position:absolute;left:166px;top:268px;font-size:88px;font-weight:700;color:var(--white);line-height:1}
.hero-sub{position:absolute;left:167px;top:374px;font-size:24px;color:var(--white)}
.apply-btn{position:absolute;left:170px;top:436px;width:130px;height:35px;border-radius:18px;background:var(--yellow);
  color:var(--white);font-size:14px;font-weight:600;display:flex;align-items:center;justify-content:center}

.contact-back{position:absolute;left:789px;top:450px;width:279px;height:401px;background:var(--yellow)}
.contact-card{position:absolute;left:771px;top:432px;width:278px;height:400px;background:var(--white);
  box-shadow:0 4px 18px rgba(0,0,0,.08);padding:22px 24px}
.contact-card h3{font-size:22px;font-weight:500;color:var(--ink);margin-bottom:20px}
.field{height:31px;background:var(--field);border-radius:2px;margin-bottom:13px;font-size:11px;color:#444;
  padding:9px 12px;position:relative}
.field.select::after{content:"";position:absolute;right:12px;top:13px;border:4px solid transparent;border-top-color:#555}
.field.msg{height:93px;margin-bottom:14px}
.send-btn{width:106px;height:34px;background:var(--yellow);color:var(--white);font-size:14px;font-weight:600;
  display:flex;align-items:center;justify-content:center}

/* intro */
.intro-title{position:absolute;left:131px;top:924px;font-size:48px;line-height:58px;color:var(--ink);font-weight:400}
.intro-title b{font-weight:800}
.intro-rule{position:absolute;left:479px;top:920px;width:1px;height:228px;background:#d9b25a}
.intro-text{position:absolute;left:543px;top:966px;width:520px;font-size:14.5px;line-height:27.7px;color:var(--text)}

/* sections */
.band{position:absolute;left:0;width:1200px;background:var(--bg-soft)}
.section-head{position:absolute;font-size:29px;font-weight:700;color:var(--navy);letter-spacing:-.2px}
.ticks{position:absolute;list-style:none}
.ticks li{position:relative;padding-left:38px;font-size:18px;line-height:23px;color:var(--text)}
.ticks li::before{content:"";position:absolute;left:3px;top:5px;width:14px;height:14px;border-radius:50%;background:var(--yellow)}
.qual-list{left:131px;top:1412px;width:380px}
.qual-list li{margin-bottom:12px}
.duty-list{left:691px;top:2678px;width:360px}
.duty-list li{margin-bottom:28px}

.photo-back{position:absolute;background:var(--yellow)}
.photo{position:absolute;box-shadow:0 4px 14px rgba(0,0,0,.15)}
.photo-mechanic{left:594px;top:1403px;width:474px;height:366px;
  background:linear-gradient(135deg,#3b2d22 0%,#6e5a45 40%,#e0592c 60%,#2f3338 100%)}
.photo-hands{left:131px;top:2596px;width:475px;height:367px;
  background:linear-gradient(100deg,#4a4f55 0%,#8d8a88 35%,#c8937a 60%,#5c3d30 100%)}

/* services wheel */
.wheel{position:absolute;left:369px;top:1959px}
.wheel-label{position:absolute;font-size:16px;font-weight:600;color:var(--ink);line-height:23px}

/* footer */
.foot-col{position:absolute;top:3136px}
.foot-col::before{content:"";display:block;width:30px;height:2px;background:var(--ink);margin-bottom:16px}
.foot-col h4{font-size:16px;font-weight:400;color:var(--ink);margin-bottom:14px}
.foot-col ul{list-style:none}
.foot-col li{font-size:11.5px;line-height:21.8px;color:var(--ink)}
.contact-row{display:flex;align-items:center;gap:10px;font-size:11.5px;color:var(--ink);margin-bottom:14px}
.news{display:flex;margin-top:4px}
.news-input{width:116px;height:26px;background:var(--bg-soft);font-size:9px;color:#777;padding:8px 10px}
.news-btn{width:28px;height:26px;background:var(--yellow);display:flex;align-items:center;justify-content:center}
.socials{display:flex;gap:5px;margin-top:32px}
.socials span{width:24px;height:24px;border-radius:50%;background:var(--ink)}
.bottom-bar{position:absolute;left:0;top:3336px;width:1200px;height:63px;background:var(--bg-soft);font-size:11.5px;color:var(--ink)}
.bottom-bar .copy{position:absolute;left:201px;top:23px}
.bottom-bar .legal{position:absolute;left:811px;top:23px}
</style>
</head>
<body>

<header>
  <div class="hero-photo" role="img" aria-label="Photo of a service technician in navy coveralls kneeling in front of a yellow excavator"></div>
  <div class="brand"><span class="brand-mark"></span><span class="brand-name">Harrow<br>Machinery</span></div>
  <nav class="nav"><a href="#">Home</a><a href="#">Contact Us</a></nav>
  <div class="phone-btn">
    <svg width="12" height="12" viewBox="0 0 24 24"><path fill="#fff" d="M6.6 10.8a15 15 0 0 0 6.6 6.6l2.2-2.2a1 1 0 0 1 1-.25 11.4 11.4 0 0 0 3.6.57 1 1 0 0 1 1 1V20a1 1 0 0 1-1 1A17 17 0 0 1 3 4a1 1 0 0 1 1-1h3.5a1 1 0 0 1 1 1c0 1.25.2 2.45.57 3.57a1 1 0 0 1-.25 1z"/></svg>
    800-555-0148
  </div>
  <h1 class="hero-title">We Hire</h1>
  <p class="hero-sub">Heavy Equipment Service Technician</p>
  <div class="apply-btn">Apply Now</div>

  <div class="contact-back"></div>
  <form class="contact-card">
    <h3>Contact Us</h3>
    <div class="field">Name</div>
    <div class="field">Email</div>
    <div class="field select">Phone</div>
    <div class="field msg">Message</div>
    <div class="send-btn">Send Us</div>
  </form>
</header>

<section>
  <h2 class="intro-title">HEAVY<br>EQUIPMENT<br><b>SERVICE<br>TECHNICIAN</b></h2>
  <div class="intro-rule"></div>
  <p class="intro-text">Lorem Ipsum is simply dummy text of the printing and typesetting industry. Lorem Ipsum has been the industry's standard dummy text ever since the 1500s, when an unknown printer took a galley of type and scrambled it to make a type specimen book. It has survived not only five centuries,</p>
</section>

<section class="band" style="top:1254px;height:631px"></section>
<h2 class="section-head" style="left:131px;top:1324px">QUALIFICATIONS AND SKILL</h2>
<ul class="ticks qual-list">
  <li>Must have a valid driver’s license.</li>
  <li>Must be reliable, hard working and have a professional work ethic.</li>
  <li>Must own tools and have the ability to work independently.</li>
  <li>Must have the ability to lift, push, pull 70+ pounds, climb heavy. equipment safely, bend and kneel.</li>
  <li>Must be able to perform basic equipment service: ie: filters, oils, inspections.</li>
  <li>Must possess a willingness to learn and grow.</li>
  <li>Must provide own tools.</li>
</ul>
<div class="photo-back" style="left:611px;top:1422px;width:474px;height:365px"></div>
<div class="photo photo-mechanic" role="img" aria-label="Photo of a mechanic in an orange hard hat working under heavy machinery"></div>

<section>
  <svg class="wheel" width="460" height="460" viewBox="0 0 460 460">
    <circle cx="230" cy="230" r="229" fill="none" stroke="#e6e7ea" stroke-width="1.5"/>
    <circle cx="230" cy="230" r="120" fill="#f5f6f8"/>
    <rect x="150" y="218" width="24" height="24" fill="#FFD400"/>
    <text x="183" y="237" font-family="Outfit, sans-serif" font-size="22" font-weight="700" fill="#111a26">Harrow</text>
    <circle cx="60" cy="74" r="7" fill="#FFD400"/>
    <circle cx="402" cy="74" r="7" fill="#FFD400"/>
    <circle cx="60" cy="381" r="7" fill="#FFD400"/>
    <circle cx="402" cy="381" r="7" fill="#FFD400"/>
  </svg>
  <div class="wheel-label" style="left:215px;top:2006px;width:160px;text-align:right">Supplying New &amp;<br>Used Equipment</div>
  <div class="wheel-label" style="left:810px;top:2015px">Equipment Rentals</div>
  <div class="wheel-label" style="left:250px;top:2329px;width:130px;text-align:right">Service</div>
  <div class="wheel-label" style="left:810px;top:2329px">Parts &amp; Advice</div>
</section>

<section class="band" style="top:2508px;height:554px"></section>
<div class="photo photo-hands" role="img" aria-label="Photo of a gloved hand holding a wrench beside a thumbs-up"></div>
<h2 class="section-head" style="left:688px;top:2606px">RESPONSIBILITIES AND DUTIES</h2>
<ul class="ticks duty-list">
  <li>Perform scheduled services on heavy equipment and tractors.</li>
  <li>Perform final assembly of tractors.</li>
  <li>Perform body work on equipment.</li>
  <li>Perform minor welding on equipment and tractors.</li>
  <li>Keep work space clean of all debris.</li>
</ul>

<footer>
  <div class="foot-col" style="left:162px">
    <h4>Site Links</h4>
    <ul><li>Harrow Machinery</li><li>Sales, Service &amp; Rentals</li><li>HOME</li><li>NEW EQUIPMENT</li><li>GENERATORS</li><li>USED EQUIPMENT</li></ul>
  </div>
  <div class="foot-col" style="left:375px">
    <h4>Site Links</h4>
    <ul><li>RENTALS</li><li>PARTS</li><li>SERVICE</li><li>SALES</li><li>ABOUT US</li><li>CONTACT US</li></ul>
  </div>
  <div class="foot-col" style="left:575px">
    <h4>Contact Us</h4>
    <div class="contact-row"><svg width="14" height="14" viewBox="0 0 24 24"><path fill="none" stroke="#111a26" stroke-width="1.6" d="M6.6 10.8a15 15 0 0 0 6.6 6.6l2.2-2.2a1 1 0 0 1 1-.25 11.4 11.4 0 0 0 3.6.57 1 1 0 0 1 1 1V20a1 1 0 0 1-1 1A17 17 0 0 1 3 4a1 1 0 0 1 1-1h3.5a1 1 0 0 1 1 1c0 1.25.2 2.45.57 3.57a1 1 0 0 1-.25 1z"/></svg>Phone:&nbsp; 800-555-0172</div>
    <div class="contact-row"><svg width="14" height="14" viewBox="0 0 24 24"><path fill="none" stroke="#111a26" stroke-width="1.6" d="M12 21s-6-6.2-6-11a6 6 0 0 1 12 0c0 4.8-6 11-6 11z"/><circle cx="12" cy="10" r="2.2" fill="none" stroke="#111a26" stroke-width="1.6"/></svg>Address, City</div>
    <div class="contact-row"><svg width="14" height="14" viewBox="0 0 24 24"><rect x="3" y="6" width="18" height="13" fill="none" stroke="#111a26" stroke-width="1.6"/><path d="M3 6l9 7 9-7" fill="none" stroke="#111a26" stroke-width="1.6"/></svg>jobs@harrow-example.com</div>
  </div>
  <div class="foot-col" style="left:892px">
    <h4>Newsletter</h4>
    <div class="news"><div class="news-input">Email...</div><div class="news-btn"><svg width="12" height="12" viewBox="0 0 24 24"><path fill="#fff" d="M2 11l20-9-9 20-2-9z"/></svg></div></div>
    <div class="socials"><span></span><span></span><span></span></div>
  </div>
  <div class="bottom-bar">
    <span class="copy">©2022 Harrowmach | &nbsp;All Rights Reserved.</span>
    <span class="legal">Terms &amp; Conditions &nbsp;| &nbsp;Privacy Policy</span>
  </div>
</footer>

</body>
</html>
```